Lantern Hour 2017 (an advertisement for a musical Christian presentation)

This postcard will advertise a Christian MUSICAL show celebrating the 2017 New Year. Graphics needs to indicate musical content, Colors are December advertising.

We will need all of the layers unlocked in PSD format
Our logo is attached

TITLE: Lantern Hour 2017
SUBTITLE: You're Invited
TIME: December 31, 2016 at 11:00PM

Target Market(s)

Christians that have been attendees to our church

Industry/Entity Type

Non-Profit

Font styles to use
Sans Serif
Script

Requirements
Must have
• Must have a modern look and feel and caught the eye in the mailbox.
• Musical content indicated in background
Nice to have
• December marketing colors
• Strong Fontology
Should not have
• Should not have styles not relevant in the US

```html
<!DOCTYPE html>
<html lang="en">
<head>
<meta charset="utf-8">
<title>Lantern Hour 2017 – Postcard</title>
<link rel="stylesheet" href="https://fonts.googleapis.com/css2?family=Oswald:wght@400;500;600;700&family=Pinyon+Script&family=Roboto+Condensed:wght@400&display=swap">
<style>
  :root{
    --backdrop:#1d1d1d;
    --paper:#ffffff;
    --ink:#1f1f1f;
    --rule:#333333;
    --stamp-line:#9a9a9a;
    --orange:#ee7d1c;
    --olive:#4a6332;
    --mark:#5a6d7d;
    --red-light:#c01f26;
    --red-dark:#6e0c12;
    --cream:#f4eea0;
    --staff:#f4eea0;
    --white:#ffffff;
  }
  html,body{margin:0;padding:0;overflow:hidden}
  body{width:1200px;height:1200px;background:var(--backdrop);position:relative;font-family:"Oswald",sans-serif}
  p{margin:0}

  .card{position:absolute;box-sizing:border-box;overflow:hidden}

  /* address side */
  .card-back{left:358px;top:38px;width:806px;height:546px;background:var(--paper)}
  .sender{position:absolute;left:22px;top:56px;display:flex;align-items:center}
  .sender-square{width:50px;height:50px;background:var(--mark);margin-right:46px}
  .sender-details{border-left:2px solid var(--rule);padding-left:10px}
  .sender-org{font-family:"Roboto Condensed",sans-serif;font-size:27px;color:var(--ink);line-height:1.15}
  .sender-address{font-family:"Roboto Condensed",sans-serif;font-size:17px;color:var(--ink);line-height:1.3}
  .stamp-box{position:absolute;right:16px;top:17px;width:162px;height:162px;border:1.5px solid var(--stamp-line);box-sizing:border-box}
  .address-lines{position:absolute;left:426px;top:283px;width:380px;height:200px}

  .back-headline{position:absolute;left:30px;top:160px;width:340px;text-align:center}
  .back-headline .invite-script{font-family:"Pinyon Script",cursive;font-size:60px;line-height:1;color:var(--orange);white-space:nowrap}
  .back-headline .title{font-weight:700;font-size:47px;line-height:1;color:var(--olive);margin:2px 0 0 40px;letter-spacing:0.5px}
  .back-headline .year{font-weight:700;font-size:146px;line-height:0.95;color:var(--olive);margin:-4px 0 0 40px;letter-spacing:-2px}
  .back-headline .when{font-weight:600;font-size:31px;line-height:1.2;color:var(--orange);margin:-2px 0 0 40px}

  /* picture side */
  .card-front{left:52px;top:620px;width:807px;height:546px;
    background:radial-gradient(ellipse at 45% 55%,var(--red-light) 0%,#9b161c 55%,var(--red-dark) 100%)}
  .music-staff{position:absolute;left:0;top:0;width:807px;height:546px}
  .front-script{position:absolute;left:30px;top:22px;font-family:"Pinyon Script",cursive;font-size:84px;line-height:1;color:var(--cream);white-space:nowrap}
  .front-event{position:absolute;left:275px;width:200px;top:262px;text-align:center;color:var(--cream)}
  .front-event .title{font-weight:700;font-size:33px;line-height:1;white-space:nowrap}
  .front-event .year{font-weight:700;font-size:98px;line-height:0.95;letter-spacing:-1px;margin-top:2px}
  .front-event .when{font-weight:500;font-size:20px;line-height:1.2;margin-top:2px;white-space:nowrap}
  .front-org{position:absolute;right:34px;bottom:26px;font-family:"Oswald",sans-serif;font-weight:500;font-size:34px;color:var(--white);line-height:1}
</style>
</head>
<body>

<section class="card card-back" aria-label="Postcard address side">
  <div class="sender">
    <span class="sender-square" aria-hidden="true"></span>
    <div class="sender-details">
      <div class="sender-org">Harbor Light Chapel</div>
      <div class="sender-address">0000 Your Street, Your City, Country, ZIP Code</div>
    </div>
  </div>
  <div class="stamp-box" aria-label="Stamp area"></div>

  <div class="back-headline">
    <p class="invite-script">You’re Invited</p>
    <p class="title">LANTERN HOUR</p>
    <p class="year">2017</p>
    <p class="when">DECEMBER 31, 2016<br>@ 11:00 PM</p>
  </div>

  <svg class="address-lines" viewBox="0 0 380 200" aria-hidden="true">
    <g stroke="#222" stroke-width="1.6">
      <line x1="0" y1="0" x2="364" y2="0"/>
      <line x1="0" y1="61" x2="364" y2="61"/>
      <line x1="0" y1="122" x2="364" y2="122"/>
      <line x1="0" y1="181" x2="364" y2="181"/>
    </g>
  </svg>
</section>

<section class="card card-front" aria-label="Postcard picture side">
  <svg class="music-staff" viewBox="0 0 807 546" role="img" aria-label="Sweeping music staff lines across the background">
    <g fill="none" stroke="var(--staff)" stroke-width="2" opacity="0.22">
      <path d="M-10 190 C 200 120, 520 300, 820 200"/>
      <path d="M-10 206 C 200 136, 520 316, 820 216"/>
      <path d="M-10 222 C 200 152, 520 332, 820 232"/>
      <path d="M-10 238 C 200 168, 520 348, 820 248"/>
      <path d="M-10 254 C 200 184, 520 364, 820 264"/>
    </g>
    <g fill="none" stroke="var(--staff)" stroke-width="2" opacity="0.14">
      <path d="M-10 430 C 240 500, 560 330, 820 420"/>
      <path d="M-10 446 C 240 516, 560 346, 820 436"/>
      <path d="M-10 462 C 240 532, 560 362, 820 452"/>
      <path d="M-10 478 C 240 548, 560 378, 820 468"/>
      <path d="M-10 494 C 240 564, 560 394, 820 484"/>
    </g>
  </svg>
  <p class="front-script">You’re Invited</p>
  <div class="front-event">
    <div class="title">LANTERN HOUR</div>
    <div class="year">2017</div>
    <div class="when">12.31.2016 @ 11:00PM</div>
  </div>
  <div class="front-org">Harbor Light Chapel</div>
</section>

</body>
</html>
```